Friendly website/webshop needed for small family store

Hello .. I really need a website that is easy to use as I have no experience with this at all. ..
My shop is called hollowmoss and I had a fantastic logo from plume yard - I asked for something mid century modern and I love it. I will attach . There might be some development around the logo now for various paraphernalia ( stickers , printed tissue paper carrier bags etc.. ) I would also like some sort of help with a slogan such as 'sing your prettiest song' as in,  live your best life etc..  but I'm not sure if this is a little trite .... ? but it would be nice to link the hollowmoss with a little Motto.    If I need to pay extra for this - please could you let me know ... I'm happy to add on payment ..
As you can see the only LOGO colours really are grey black and orange .. so I would like some ideas to expand on the bird  to bring in some more colours.....  the tag line flower.children.home I would like to drop..
* the original brief included flowers on the tag line  because at the time we were also a florist . we now just sell dried flowers
My shop is in the beautiful town of Malvern, we have lots of tourist that come to walk the hills and enjoy nature - it's a family and dog friendly sort of town and we are a dog and family friendly sort of shop :-) It's a relaxed space that focuses on beautiful handmade items such as baskets & wooden utensils  from Africa, textiles from India and ceramics from France, Portugal and Italy.  We have a lovely section for children that sells beautiful soft toys from Tevare Lusin and the wonderful mice family and bunnies from Orvasi.
We stock TOLVA homeware which is lovely and earthy and natural.
We would like to communicate the value of buying thoughtfully  and conscientiously, of building a beautiful home whilst investing in & supporting makers world wide. We don't sell anything that can't be repurposed, recycled etc..
Thank you

```html
<!DOCTYPE html>
<html lang="en">
<head>
<meta charset="utf-8">
<title>hollowmoss — sing your prettiest song</title>
<link href="https://fonts.googleapis.com/css2?family=Comfortaa:wght@400;500;600&family=Montserrat:wght@400;500;600;700&display=swap" rel="stylesheet">
<style>
:root{
  --terracotta:#d08a7b;
  --slate:#74809b;
  --teal:#7cb3c2;
  --ink:#3b3b3d;
  --text:#444;
  --blush:#faf3f0;
  --card:#eeeded;
  --field:#f2f2f2;
  --black:#000;
  --white:#fff;
}
*{box-sizing:border-box;margin:0;padding:0}
html,body{width:1200px;height:3954px;overflow:hidden;background:var(--white)}
body{font-family:"Montserrat",sans-serif;color:var(--text);position:relative}
.display{font-family:"Comfortaa",sans-serif;text-transform:uppercase;white-space:nowrap}
.t1{color:var(--terracotta)}.t2{color:var(--slate)}.t3{color:var(--teal)}
.btn{display:inline-flex;align-items:center;justify-content:center;background:var(--terracotta);color:var(--white);border-radius:28px;font-weight:600;font-size:18px;letter-spacing:.5px}

/* hero */
.hero{position:absolute;left:0;top:0;width:1200px;height:690px;background:linear-gradient(100deg,#bcb8b2 0%,#d8d3cd 35%,#e1dcd7 60%,#dcd7d2 100%)}
.hero-photo{position:absolute;left:0;top:0;width:560px;height:690px;background:radial-gradient(ellipse at 45% 40%,#efeadf 0%,#b8a68a 35%,rgba(185,175,160,0) 70%)}
.hero-floor{position:absolute;left:0;bottom:0;width:1200px;height:90px;background:linear-gradient(#d7d1ca,#e6e1dc)}
.nav{position:absolute;top:62px;font-size:16px;font-weight:500;color:var(--ink);display:flex;gap:36px}
.nav .active{color:var(--slate)}
.logo{position:absolute;left:480px;top:40px;width:240px;text-align:center}
.logo .dot{width:38px;height:38px;border-radius:50%;background:var(--slate);margin:0 auto 16px}
.logo .name{font-weight:700;font-size:34px;color:var(--ink);line-height:1}
.hero-copy{position:absolute;left:571px;top:248px}
.hero-copy .l1{font-size:36px;color:var(--ink);font-weight:500}
.hero-copy .l2{font-size:50px;margin-top:36px;font-weight:500}
.hero-copy .l3{font-size:50px;margin-top:30px;color:var(--ink);font-weight:500}
.hero-copy .btn{margin-top:42px;width:170px;height:52px}

/* categories */
.cat{position:absolute;top:784px;width:316px;height:189px;background:var(--card);padding:48px 0 0 21px}
.cat .label{font-size:16px;font-weight:500;line-height:30px;text-transform:uppercase}
.cat .shop{margin-top:12px;font-size:14px;font-weight:700;color:var(--ink);display:flex;align-items:center;gap:8px}
.cat .shop span{text-decoration:underline}
.cat .img{position:absolute;right:18px;top:20px;width:150px;height:150px}

/* about */
.about-frame{position:absolute;left:110px;top:1068px;width:498px;height:397px;border:2px solid var(--terracotta);border-bottom-left-radius:40px;border-top-right-radius:40px;border-left:none;border-top:none}
.about-photo{position:absolute;left:110px;top:1068px;width:490px;height:388px;border-bottom-left-radius:40px;border-top-right-radius:40px;background:linear-gradient(180deg,#c9cbd0 0%,#9aa0a8 45%,#6c6b6a 85%,#4c4f56 100%)}
.about h2{position:absolute;left:680px;top:1076px;font-size:35px;font-weight:500}
.about p{position:absolute;left:681px;top:1136px;width:420px;font-size:16.5px;line-height:35px;color:var(--ink)}
.about .btn{position:absolute;left:681px;top:1404px;width:170px;height:53px}

/* products */
.shop-band{position:absolute;left:0;top:1562px;width:1200px;height:740px;background:var(--blush)}
.sec-title{position:absolute;left:0;width:1200px;text-align:center;font-size:36px;font-weight:500}
.prod{position:absolute;top:1720px;width:318px;height:419px;border-radius:22px 22px 0 0;padding:10px 10px 0;text-align:center;color:var(--white)}
.prod.p1{background:var(--terracotta);border-top-right-radius:0;border-bottom-left-radius:22px}
.prod.p2{background:var(--slate);border-top-left-radius:0;border-top-right-radius:0}
.prod.p3{background:var(--teal);border-top-left-radius:0}
.prod .img{width:298px;height:218px}
.prod h3{margin-top:28px;font-size:16px;font-weight:600;letter-spacing:.5px}
.prod p{margin-top:14px;font-size:14.5px;line-height:29px;opacity:.95}
.prod .price{display:inline-block;margin-top:14px;background:var(--white);border-radius:20px;padding:9px 20px;font-weight:600;font-size:16px}
.p1 .price{color:var(--terracotta)}.p2 .price{color:var(--slate)}.p3 .price{color:var(--teal)}
.circ{position:absolute;top:2193px;width:40px;height:40px;border:2px solid var(--terracotta);border-radius:50%;display:flex;align-items:center;justify-content:center}

/* testimonial */
.testi{position:absolute;left:132px;top:2489px;width:936px;height:393px;border-radius:26px 0 26px 26px;overflow:hidden}
.testi-quote{position:absolute;left:0;top:0;width:445px;height:393px;background:var(--terracotta);color:var(--white);text-align:center;padding-top:42px}
.testi-quote .mark{font-family:Georgia,serif;font-size:80px;line-height:60px;font-weight:700}
.stars{margin-top:14px;display:flex;justify-content:center}
.testi-quote p{margin-top:14px;font-size:16.5px;line-height:40px;padding:0 16px}
.testi-quote .who{margin-top:4px;font-size:21px;letter-spacing:1.5px}
.testi-photo{position:absolute;left:445px;top:0;width:491px;height:393px;background:radial-gradient(ellipse at 50% 55%,#f2c9a6 0%,#f6d6bb 55%,#f8dcc4 100%);border-top-right-radius:26px}
.arrow-sq{position:absolute;top:2671px;width:31px;height:31px;background:var(--ink);display:flex;align-items:center;justify-content:center}

/* contact */
.ci{position:absolute;top:3057px}
.ci .h{display:flex;align-items:center;gap:16px;font-size:19px;font-weight:500;color:var(--terracotta)}
.ci.two .h,.ci.three .h{color:var(--slate)}
.ci .v{margin-top:20px;margin-left:43px;font-size:16.5px;font-weight:500;color:var(--ink);line-height:38px;white-space:nowrap}
.field{position:absolute;left:110px;width:477px;height:63px;background:var(--field);border:1.5px solid #dcdcdc;border-radius:3px;padding:20px 30px;font-size:17px;font-weight:500;color:var(--ink)}
.form .btn{position:absolute;left:110px;top:3581px;width:172px;height:52px}
.map-frame{position:absolute;left:618px;top:3200px;width:472px;height:464px;border:2px solid var(--terracotta);border-top:none;border-right:none;border-bottom-right-radius:38px;border-top-left-radius:26px}
.map{position:absolute;left:625px;top:3200px;width:465px;height:455px;border-top-left-radius:26px;border-bottom-right-radius:36px;background:linear-gradient(135deg,#f1ebe0 0%,#efe6d7 40%,#eae4dc 70%,#f0ebe5 100%)}

/* footer */
.footer{position:absolute;left:0;top:3749px;width:1200px;height:205px;background:var(--black);color:var(--white)}
.f-logo{position:absolute;left:140px;top:38px;width:195px;text-align:center}
.f-logo .dot{width:34px;height:34px;border-radius:50%;background:var(--slate);margin:0 auto 16px}
.f-logo .name{font-weight:700;font-size:32px;line-height:1;color:var(--white)}
.f-links{position:absolute;right:150px;top:68px;font-size:15px;font-weight:500;display:flex;gap:16px;color:var(--white)}
.f-copy{position:absolute;right:150px;top:120px;font-size:14.5px;font-weight:500;color:var(--white)}
</style>
</head>
<body>

<header class="hero">
  <div class="hero-photo" role="img" aria-label="Woven jug vase of white dried flowers with a linen cloth on a pale wooden table"></div>
  <div class="hero-floor"></div>
  <nav class="nav" style="left:164px"><span class="active">HOME</span><span>ABOUT US</span><span>PRODUCTS</span></nav>
  <nav class="nav" style="left:758px"><span>TESTIMONIALS</span><span>CONTACT US</span>
    <svg width="20" height="20" viewBox="0 0 20 20" style="margin-left:4px"><circle cx="8" cy="8" r="6" fill="none" stroke="#3b3b3d" stroke-width="2"/><line x1="12.5" y1="12.5" x2="18" y2="18" stroke="#3b3b3d" stroke-width="2"/></svg>
  </nav>
  <div class="logo">
    <div class="dot"></div>
    <div class="name">hollowmoss</div>
  </div>
  <div class="hero-copy">
    <div class="display l1">Welcome to hollowmoss</div>
    <div class="display l2"><span class="t1">Sing</span> <span class="t2">your</span> <span class="t3">prettiest</span></div>
    <div class="display l3">Song</div>
    <a class="btn">GET STARTED</a>
  </div>
</header>

<section class="categories">
  <div class="cat" style="left:110px">
    <div class="label t1">Handmade<br>Baskets</div>
    <div class="shop"><span>SHOP NOW</span>→</div>
    <div class="img" role="img" aria-label="Round woven basket" style="top:45px;height:100px;background:radial-gradient(ellipse,#8a5a35 0%,#a87046 50%,rgba(238,237,237,0) 72%)"></div>
  </div>
  <div class="cat" style="left:442px">
    <div class="label t2">Wooden<br>Utensils</div>
    <div class="shop"><span>SHOP NOW</span>→</div>
    <div class="img" role="img" aria-label="Wooden spoons and forks in a pot with a plant" style="background:radial-gradient(ellipse,#e2c39c 0%,#d9b38a 45%,rgba(238,237,237,0) 72%)"></div>
  </div>
  <div class="cat" style="left:773px">
    <div class="label t3">TOLVA<br>Homeware</div>
    <div class="shop"><span>SHOP NOW</span>→</div>
    <div class="img" role="img" aria-label="Brown upholstered armchair" style="background:radial-gradient(ellipse,#5b3d2d 0%,#6e4b37 45%,rgba(238,237,237,0) 72%)"></div>
  </div>
</section>

<section class="about">
  <div class="about-frame"></div>
  <div class="about-photo" role="img" aria-label="Shop front with large windows and baskets and chairs outside"></div>
  <h2 class="display"><span class="t1">About</span> <span class="t2">hollowmoss</span></h2>
  <p>Lorem ipsum dolor sit amet, consectetur adipiscing elit, sed do eiusmod tempor incididunt ut labore et dolore magna aliqua. Ut enim ad minim veniam, quis nostrud exercitation ullamco laboris nisi ut aliquip ex ea commodo consequat. Duis aute irure dolor in reprehenderit in voluptate velit esse cillum.</p>
  <a class="btn">LEARN MORE</a>
</section>

<section class="shop-band"></section>
<h2 class="sec-title display" style="top:1620px"><span class="t1">Shop</span> <span class="t2">Handpicked</span> <span class="t3">for you</span></h2>
<div class="prod p1" style="left:110px">
  <div class="img" role="img" aria-label="Shop interior with colourful woven baskets and cushions" style="background:linear-gradient(135deg,#d0b79a,#9c6a4b 50%,#c79f83)"></div>
  <h3>LOREM IPSUM DOLOR</h3><p>Lorem ipsum dolor sit amet,<br>consectetur adipiscing</p><span class="price">$ 67.98</span>
</div>
<div class="prod p2" style="left:442px">
  <div class="img" role="img" aria-label="Soft toy mice with macarons on a tray" style="background:linear-gradient(135deg,#8d8072,#c9b7a2 50%,#a55d45)"></div>
  <h3>LOREM IPSUM DOLOR</h3><p>Lorem ipsum dolor sit amet,<br>consectetur adipiscing</p><span class="price">$ 98.89</span>
</div>
<div class="prod p3" style="left:771px">
  <div class="img" role="img" aria-label="Shelves of ceramics and dried flowers" style="background:linear-gradient(135deg,#5c4a3d,#cfc2b1 55%,#8e8a7d)"></div>
  <h3>LOREM IPSUM DOLOR</h3><p>Lorem ipsum dolor sit amet,<br>consectetur adipiscing</p><span class="price">$ 89.12</span>
</div>
<div class="circ" style="left:549px"><svg width="14" height="14" viewBox="0 0 14 14"><path d="M9 2 4 7l5 5" fill="none" stroke="#d08a7b" stroke-width="1.8"/></svg></div>
<div class="circ" style="left:610px"><svg width="14" height="14" viewBox="0 0 14 14"><path d="M5 2l5 5-5 5" fill="none" stroke="#d08a7b" stroke-width="1.8"/></svg></div>

<h2 class="sec-title display" style="top:2384px"><span class="t1">What</span> <span class="t2">customer</span> <span class="t3">says</span></h2>
<section class="testi">
  <div class="testi-quote">
    <div class="mark">“</div>
    <div class="stars">
      <svg width="90" height="16" viewBox="0 0 90 16"><g fill="#fff"><path id="star" d="M8 0l2.4 5 5.6.6-4.2 3.8 1.2 5.6L8 12.2 3 15l1.2-5.6L0 5.6 5.6 5z"/><use href="#star" x="18.5"/><use href="#star" x="37"/><use href="#star" x="55.5"/><use href="#star" x="74"/></g></svg>
    </div>
    <p>Sed ut perspiciatis unde omnis iste natus error<br>sit voluptatem accusantium doloremque<br>laudantium, totam rem aperiam, eaque ipsa<br>quae ab illo inventore veritatis et quasi</p>
    <div class="who">LOREM LIPSUM</div>
  </div>
  <div class="testi-photo" role="img" aria-label="Smiling customer in a navy t-shirt with arms crossed"></div>
</section>
<div class="arrow-sq" style="left:133px"><svg width="14" height="12" viewBox="0 0 14 12"><path d="M13 6H2M6 1 1 6l5 5" fill="none" stroke="#fff" stroke-width="1.8"/></svg></div>
<div class="arrow-sq" style="left:1035px"><svg width="14" height="12" viewBox="0 0 14 12"><path d="M1 6h11M8 1l5 5-5 5" fill="none" stroke="#fff" stroke-width="1.8"/></svg></div>

<h2 class="sec-title display" style="top:2970px"><span class="t1">Contact</span> <span class="t2">us</span></h2>
<section class="contact">
  <div class="ci one" style="left:110px">
    <div class="h"><svg width="22" height="26" viewBox="0 0 22 26"><path d="M11 1a8 8 0 0 0-8 8c0 6 8 12 8 12s8-6 8-12a8 8 0 0 0-8-8z" fill="#d08a7b"/><circle cx="11" cy="9" r="3" fill="#fff"/><ellipse cx="11" cy="23" rx="9" ry="2.4" fill="none" stroke="#d08a7b" stroke-width="1.5"/></svg>ADDRESS</div>
    <div class="v">LEVEL 13, 198 LOREMLIPSUM SIT,<br>ZDE 2000 LOREM</div>
  </div>
  <div class="ci two" style="left:534px">
    <div class="h"><svg width="22" height="22" viewBox="0 0 22 22"><path d="M4 1l4 4-2.5 3c1.5 3.5 4 6 7.5 7.5L16 13l4 4-3 4C9 20 2 13 1 4z" fill="#74809b"/></svg>CALL US</div>
    <div class="v">01632 960418</div>
  </div>
  <div class="ci three" style="left:821px">
    <div class="h"><svg width="22" height="16" viewBox="0 0 22 16"><rect x="1" y="1" width="20" height="14" fill="#74809b"/><path d="M1 1l10 8 10-8" fill="none" stroke="#fff" stroke-width="1.5"/></svg>MAIL US</div>
    <div class="v">HELLO@HOLLOWMOSS.SHOP</div>
  </div>
</section>
<form class="form">
  <div class="field" style="top:3200px">FULL NAME</div>
  <div class="field" style="top:3280px">EMAIL ADDRESS</div>
  <div class="field" style="top:3359px">PHONE NUMBER</div>
  <div class="field" style="top:3436px;height:114px">MESSAGE</div>
  <a class="btn">SUBMIT NOW</a>
</form>
<div class="map-frame"></div>
<div class="map" role="img" aria-label="Street map showing the shop location"></div>

<footer class="footer">
  <div class="f-logo">
    <div class="dot"></div>
    <div class="name">hollowmoss</div>
  </div>
  <div class="f-links"><span>HOME</span>|<span>ABOUT US</span>|<span>PRODUCTS</span>|<span>TESTIMONIALS</span>|<span>CONTACT US</span></div>
  <div class="f-copy">@2024 COPYRIGHTS - ALL RIGHTS RESERVED</div>
</footer>

</body>
</html>
```